Health Care Service Company Flyer

Company name: Bright Harbor Clinic
Slogan: Find out what you're made of
Website: brightharborclinic.ca

I need the flyer to contain the company name (will provide logo source file ASAP), the slogan in large font and a "find out more at harborclinic.ca"

Other important data to include in the flyer is:
Four bullet points with the following information:
*Track performance and fitness results over time
*Develop proprietary exercise and dietary programs based on actionable data
*Track muscle atrophy from injury, as well as muscle gain during rehabilitation
*Reveal imbalances in muscle symmetry and strength, flexibility, and joint mechanics

I also need the following information conveyed somewhere on the flyer:
*Body Fat, Muscle Mass, and Bone Density Measurements
• Over 50 data points generated in each 10 minute scan
*Call XXX-XXX-XXX to book an appointment today

DEXA Body Composition Services.
Get scanned today.

See example of competitor flyers in the images to get an example of the images and information we are trying to convey

Target Market(s)

athletes, fitness enthusiast, crossfit

Industry/Entity Type

Health And Wellness

Colors
33a6d7
acd036

Requirements
Nice to have
• Prefer images be general health and wellness related - in other words, individuals who look healthy, but are not abnormally muscular
Should not have
• Shirtless models, No big muscles,

```html
<!DOCTYPE html>
<html lang="en">
<head>
<meta charset="utf-8">
<title>Bright Harbor Clinic – Flyer</title>
<link href="https://fonts.googleapis.com/css2?family=Alfa+Slab+One&family=Cabin:wght@400;600&family=Roboto+Condensed:wght@600;700&display=swap" rel="stylesheet">
<style>
  :root {
    --blue: #33a6d7;
    --lime: #acd036;
    --white: #ffffff;
    --ink: #2b2b2b;
    --dark-band: #1f2a0e;
    --icon-grey: #6b6b6b;
    --label: #3a3a3a;
  }
  * { margin: 0; padding: 0; box-sizing: border-box; }
  html, body { width: 707px; height: 1200px; overflow: hidden; background: #e9e9e9; }
  .flyer { position: relative; width: 707px; height: 1200px; background: var(--white); overflow: hidden; font-family: "Cabin", sans-serif; }
  .shapes { position: absolute; inset: 0; width: 707px; height: 1200px; }

  .brand { position: absolute; left: 18px; top: 88px; display: flex; flex-direction: column; align-items: flex-start; gap: 10px; }
  .brand-dot { width: 46px; height: 46px; border-radius: 50%; background: var(--lime); }
  .brand-name { font-family: "Alfa Slab One", serif; font-size: 15px; color: var(--ink); letter-spacing: .3px; }

  .benefits { position: absolute; left: 28px; top: 748px; width: 320px; color: var(--white); }
  .benefits-title { font-family: "Alfa Slab One", serif; font-size: 21px; letter-spacing: .5px; padding-bottom: 3px; border-bottom: 2px solid var(--white); display: inline-block; margin-bottom: 14px; }
  .benefits-list { list-style: none; }
  .benefits-list li { position: relative; padding-left: 17px; font-size: 14px; line-height: 1.3; margin-bottom: 17px; }
  .benefits-list li::before { content: ""; position: absolute; left: 2px; top: 6px; width: 6px; height: 6px; border-radius: 50%; background: var(--white); }

  .scan-note { position: absolute; left: 0; top: 1023px; width: 360px; height: 60px; display: flex; flex-direction: column; justify-content: center; align-items: center; font-family: "Roboto Condensed", sans-serif; font-weight: 700; font-size: 19px; line-height: 1.2; color: var(--dark-band); text-transform: uppercase; }

  .booking { position: absolute; left: 0; top: 1083px; width: 360px; height: 117px; display: flex; flex-direction: column; justify-content: center; padding-left: 46px; color: var(--white); font-family: "Roboto Condensed", sans-serif; }
  .booking-phone { font-size: 38px; font-weight: 700; letter-spacing: 1px; line-height: 1; }
  .booking-text { font-size: 18px; font-weight: 600; text-transform: uppercase; margin-top: 6px; }

  .slogan { position: absolute; left: 378px; top: 820px; width: 320px; font-family: "Alfa Slab One", serif; color: var(--blue); text-transform: uppercase; line-height: 1.12; }
  .slogan span { display: block; }
  .slogan .big { font-size: 44px; }
  .slogan .mid { font-size: 32px; margin: 4px 0; }

  .measures { position: absolute; left: 362px; top: 1025px; width: 345px; height: 126px; display: flex; }
  .measure { flex: 1; display: flex; flex-direction: column; align-items: center; border-right: 1px solid #cfcfcf; }
  .measure:last-child { border-right: none; }
  .measure svg { width: 58px; height: 64px; }
  .measure-label { margin-top: 20px; font-size: 12px; color: var(--label); text-transform: uppercase; text-align: center; line-height: 1.25; }

  .site { position: absolute; left: 360px; top: 1166px; width: 347px; height: 34px; display: flex; align-items: center; justify-content: center; gap: 8px; font-size: 15px; color: var(--ink); }
  .site-dot { width: 14px; height: 14px; border-radius: 50%; background: var(--ink); }
</style>
</head>
<body>
<main class="flyer">
  <svg class="shapes" viewBox="0 0 497 700" preserveAspectRatio="none" aria-hidden="false">
    <!-- colour blocks -->
    <polygon points="265,0 497,0 497,325 263,445" fill="var(--blue)"/>
    <polygon points="0,110 100,150 100,345 0,385" fill="var(--lime)"/>
    <polygon points="0,420 88,383 263,465 253,700 0,700" fill="var(--blue)"/>
    <polygon points="78,362 263,452 497,330 497,350 263,470 70,378" fill="var(--lime)"/>
    <polygon points="253,460 497,340 497,700 253,700" fill="var(--white)"/>
    <polygon points="420,408 440,398 440,418" fill="var(--blue)"/>
    <polygon points="393,445 415,430 415,450" fill="var(--lime)"/>
    <rect x="0" y="597" width="253" height="35" fill="var(--lime)"/>
    <rect x="253" y="680" width="244" height="20" fill="var(--lime)"/>
    <!-- photo frame -->
    <polygon points="263,45 446,145 446,350 263,440 80,350 80,145" fill="var(--white)"/>
    <defs>
      <linearGradient id="photoTone" x1="0" y1="0" x2="1" y2="1">
        <stop offset="0" stop-color="#6a4a2e"/>
        <stop offset=".45" stop-color="#c9b79a"/>
        <stop offset=".75" stop-color="#e6e0d4"/>
        <stop offset="1" stop-color="#a89a86"/>
      </linearGradient>
    </defs>
    <polygon role="img" aria-label="Photo: two people stretching side by side in a bright gym studio" points="263,56 437,150 437,345 263,430 89,345 89,150" fill="url(#photoTone)"/>
  </svg>

  <div class="brand">
    <span class="brand-dot"></span>
    <span class="brand-name">BRIGHT HARBOR CLINIC</span>
  </div>

  <section class="benefits">
    <h2 class="benefits-title">WHAT WE GET?</h2>
    <ul class="benefits-list">
      <li>Track performance and fitness<br>results over time</li>
      <li>Develop proprietary exercise and dietary<br>programs based on actionable data</li>
      <li>Track muscle atrophy from injury, as well as<br>muscle gain during rehabilitation</li>
      <li>Reveal imbalances in muscle symmetry and<br>strength, flexibility, and joint mechanics</li>
    </ul>
  </section>

  <div class="scan-note">
    <span>Over 50 data points</span>
    <span>generated in each 10 minute scan</span>
  </div>

  <div class="booking">
    <span class="booking-phone">555 014 2786</span>
    <span class="booking-text">To book an appointment today</span>
  </div>

  <h1 class="slogan">
    <span class="big">Find out</span>
    <span class="mid">What you're</span>
    <span class="big">Made of</span>
  </h1>

  <div class="measures">
    <div class="measure">
      <svg viewBox="0 0 58 64"><polygon points="29,2 56,17 56,47 29,62 2,47 2,17" fill="var(--icon-grey)"/></svg>
      <span class="measure-label">Body Fat</span>
    </div>
    <div class="measure">
      <svg viewBox="0 0 58 64"><polygon points="29,2 56,17 56,47 29,62 2,47 2,17" fill="var(--icon-grey)"/></svg>
      <span class="measure-label">Muscle Mass</span>
    </div>
    <div class="measure">
      <svg viewBox="0 0 58 64"><polygon points="29,2 56,17 56,47 29,62 2,47 2,17" fill="var(--icon-grey)"/></svg>
      <span class="measure-label">Bone Density<br>Measurements</span>
    </div>
  </div>

  <div class="site">
    <span class="site-dot"></span>
    <span>brightharborclinic.ca</span>
  </div>
</main>
</body>
</html>
```